Post card for landscape service

Velmora Property Management**FEATURED SERVICE*** Weekly Lawn mowing service starting at $15/ cutting ****other services****landscape servicespring and fall clean uplawn and flowerbed care (pest and weed control)fertilizing plantingand moreCall for a Free estimate!!10% off first months service with signed contract

Please make double sided ( a front and a back)

Target Market(s)

home owners

Industry/Entity Type

Landscape

Requirements
Must have
• please feture the weekly lawn mowing service and then list the other sevices
• contact info... can be found on business card that was uploaded.
• must say residential services
Should not have
• please dont list reo management

```html
<!DOCTYPE html>
<html lang="en">
<head>
<meta charset="utf-8">
<title>Velmora Property Management – Postcard</title>
<link href="https://fonts.googleapis.com/css2?family=Roboto+Condensed:ital,wght@0,400;0,700;1,400;1,700&family=Roboto:ital,wght@0,400;0,700;1,400;1,700&display=swap" rel="stylesheet">
<style>
:root{
  --green:#1f8f3f;
  --green-dark:#14702f;
  --green-light:#3aaa4c;
  --ink:#1d1d1d;
  --white:#ffffff;
  --stage:#ecebe7;
  --line:#b9b9b9;
  --grass-a:#7fcf3a;
  --grass-b:#3f9e22;
}
*{margin:0;padding:0;box-sizing:border-box}
html,body{width:907px;height:1200px;overflow:hidden}
body{background:var(--stage);font-family:"Roboto",Arial,sans-serif;color:var(--ink);position:relative}
.card{position:absolute;background:var(--white);overflow:hidden;box-shadow:0 4px 14px rgba(0,0,0,.25)}
.front{left:120px;top:35px;width:720px;height:520px}
.back{left:118px;top:635px;width:692px;height:497px}
.fill{position:absolute}
.photo-house{left:0;top:0;width:328px;height:240px;background:linear-gradient(180deg,#9cc7ee 0%,#cfe1d0 30%,#6f9a52 55%,#4f9a2e 100%)}
.photo-sod{left:335px;top:0;width:385px;height:330px;background:linear-gradient(135deg,#6fa94a 0%,#8a7a5e 45%,#4f8f2f 100%)}
.rule-left{left:0;top:248px;width:328px;height:7px;background:var(--green)}
.front-panel{position:absolute;left:0;top:0;width:720px;height:520px}
.brand{position:absolute;left:20px;top:282px;font-family:"Roboto Condensed",sans-serif;font-weight:700;font-size:66px;line-height:1;color:var(--ink);letter-spacing:-1px}
.brand-sub{position:absolute;left:21px;top:360px;font-family:"Roboto Condensed",sans-serif;font-size:21px;color:var(--green);letter-spacing:.2px}
.brand-tag{position:absolute;left:21px;top:385px;font-family:"Roboto Condensed",sans-serif;font-weight:700;font-size:10.5px}
.bullets{position:absolute;list-style:none;font-family:"Roboto",sans-serif;font-style:italic;font-size:10.5px;font-weight:500}
.bullets li{position:relative;padding-left:14px;margin-bottom:6px}
.bullets li::before{content:"";position:absolute;left:2px;top:4px;width:6px;height:6px;border-radius:50%;background:var(--green)}
.bullets li.more{padding-left:14px;color:var(--green);font-weight:700;font-size:9.5px}
.bullets li.more::before{display:none}
.list-a{left:20px;top:412px}
.list-b{left:155px;top:412px}
.grass{background:linear-gradient(180deg,rgba(127,207,58,0) 0%,var(--grass-a) 45%,var(--grass-b) 100%)}
.grass-front{left:0;top:460px;width:330px;height:60px}
.badge{position:absolute;left:262px;top:190px;width:134px;height:134px;border-radius:50%;background:var(--white);border:5px solid var(--green);box-shadow:0 0 0 4px var(--white);text-align:center;padding-top:30px}
.badge-big{font-family:"Roboto Condensed",sans-serif;font-weight:700;font-size:28px;line-height:1}
.badge-small{font-family:"Roboto Condensed",sans-serif;font-weight:700;font-size:9.5px;color:var(--green);line-height:1.3;margin-top:6px}
.offer{position:absolute;left:347px;top:363px;width:285px;height:70px;border:2px dashed var(--white);border-radius:6px;color:var(--white);display:flex;align-items:center;padding-left:20px}
.offer-text{font-family:"Roboto Condensed",sans-serif;font-weight:700;font-size:17px;line-height:1.2}
.offer-price{font-family:"Roboto Condensed",sans-serif;font-weight:700;font-size:48px;margin-left:14px}
.contacts{position:absolute;left:345px;top:449px;width:360px;color:var(--white);font-size:9.5px;font-family:"Roboto",sans-serif}
.contact{position:absolute;display:flex;align-items:flex-start;gap:8px;white-space:nowrap}
.contact svg{flex:none;margin-top:1px}
.photo-mower{left:0;top:0;width:384px;height:195px;background:linear-gradient(180deg,#8a9a7a 0%,#9ccf6a 40%,#4ea82c 100%)}
.photo-hands{left:267px;top:183px;width:140px;height:127px;border:5px solid var(--white);box-shadow:0 2px 8px rgba(0,0,0,.35);background:linear-gradient(180deg,#4f9a2e 0%,#6e5a44 100%)}
.stripe-v{left:388px;top:0;width:6px;height:497px;background:var(--green)}
.services-head{position:absolute;left:0;top:203px;width:266px;height:67px;background:var(--green);border-bottom:3px solid var(--green-dark);color:var(--white);font-family:"Roboto Condensed",sans-serif;font-size:22px;line-height:1.3;padding:7px 0 0 16px}
.list-c{left:16px;top:286px;font-size:11px}
.list-c li{margin-bottom:8px}
.list-c li.more{margin-top:-3px;font-size:8.5px}
.cta{position:absolute;left:0;top:365px;width:348px;height:55px;background:linear-gradient(180deg,var(--green-light),var(--green-dark));border-radius:0 10px 10px 0;color:var(--white);display:flex;align-items:center;padding-left:14px;gap:14px}
.cta-text{font-family:"Roboto",sans-serif;font-style:italic;font-weight:700;font-size:13px}
.cta-phone{font-family:"Roboto Condensed",sans-serif;font-weight:700;font-size:27px}
.grass-back{left:0;top:435px;width:388px;height:62px}
.stamp{left:574px;top:51px;width:84px;height:96px;border:1px solid var(--line)}
.address-line{left:450px;width:218px;height:1px;background:var(--line)}
</style>
</head>
<body>

<section class="card front">
  <div class="fill photo-house" role="img" aria-label="Photo of a stone house with a wide green lawn and flowerbeds"></div>
  <div class="fill photo-sod" role="img" aria-label="Photo of a gardener with a lawn mower beside a roll of fresh sod"></div>
  <svg class="front-panel" viewBox="0 0 720 520" aria-hidden="true">
    <polygon points="0,255 330,255 330,262 720,262 720,520 0,520" fill="#ffffff"/>
    <polygon points="327,305 560,305 610,260 720,260 720,520 327,520" fill="#1f8f3f"/>
    <polygon points="560,305 610,260 720,260 720,270 616,270 570,312 327,312 327,305" fill="#14702f"/>
    <polygon points="640,330 720,250 720,300 690,330" fill="#ffffff"/>
    <rect x="0" y="248" width="328" height="7" fill="#1f8f3f"/>
  </svg>
  <div class="fill grass grass-front" role="img" aria-label="Strip of green grass blades"></div>
  <div class="brand">Velmora</div>
  <div class="brand-sub">PROPERTY MANAGEMENT</div>
  <div class="brand-tag">Commercial and Residential Property Management Services</div>
  <ul class="bullets list-a">
    <li>Landscap Maintenance</li>
    <li>Lawn care</li>
    <li>Property Preservation</li>
  </ul>
  <ul class="bullets list-b">
    <li>Snow and Ice Management</li>
    <li class="more">and more</li>
  </ul>
  <div class="badge">
    <div class="badge-big">10% OFF</div>
    <div class="badge-small">FIRST MONTHS SERVICE<br>WITH SIGNED CONTRACT</div>
  </div>
  <div class="offer">
    <div class="offer-text">Weekly Lawn mowing<br>service starting at</div>
    <div class="offer-price">$15</div>
  </div>
  <div class="contacts">
    <div class="contact" style="left:0;top:0">
      <svg width="10" height="10" viewBox="0 0 24 24"><path fill="#fff" d="M6.6 10.8a15 15 0 0 0 6.6 6.6l2.2-2.2a1 1 0 0 1 1-.25 11.4 11.4 0 0 0 3.6.57 1 1 0 0 1 1 1V20a1 1 0 0 1-1 1A17 17 0 0 1 3 4a1 1 0 0 1 1-1h3.5a1 1 0 0 1 1 1c0 1.25.2 2.45.57 3.6a1 1 0 0 1-.25 1z"/></svg>
      <span>908-555-0172</span>
    </div>
    <div class="contact" style="left:0;top:18px">
      <svg width="10" height="10" viewBox="0 0 24 24"><path fill="#fff" d="M12 3 2 12h3v9h5v-6h4v6h5v-9h3z"/></svg>
      <span>PO Box 418<br>Brookfield, NJ 08800</span>
    </div>
    <div class="contact" style="left:122px;top:0">
      <svg width="10" height="9" viewBox="0 0 24 20"><path fill="#fff" d="M0 2h24v16H0zM2 4l10 7 10-7"/><path fill="none" stroke="#1f8f3f" stroke-width="2" d="M1 3l11 8 11-8"/></svg>
      <span>velmoraproperty@mail.com</span>
    </div>
    <div class="contact" style="left:122px;top:18px">
      <svg width="10" height="10" viewBox="0 0 24 24"><circle cx="12" cy="12" r="10" fill="none" stroke="#fff" stroke-width="2"/><path d="M2 12h20M12 2c3 3 3 17 0 20M12 2c-3 3-3 17 0 20" fill="none" stroke="#fff" stroke-width="1.6"/></svg>
      <span>www.velmorapropertymanagement.com</span>
    </div>
  </div>
</section>

<section class="card back">
  <div class="fill photo-mower" role="img" aria-label="Photo of a lawn mower on a freshly cut green lawn with flowerbeds"></div>
  <div class="fill stripe-v"></div>
  <div class="services-head">OUR OTHER SERVICES<br>ARE AS FOLLOWS</div>
  <div class="fill photo-hands" role="img" aria-label="Photo of hands laying a piece of sod on soil"></div>
  <ul class="bullets list-c">
    <li>Fall clean up</li>
    <li>Lawn and flowerbed care<br>(pest and weed control)</li>
    <li class="more">and many more</li>
  </ul>
  <div class="cta">
    <span class="cta-text">Call for a Free estimate!!</span>
    <span class="cta-phone">908-555-0172</span>
  </div>
  <div class="fill grass grass-back" role="img" aria-label="Strip of green grass blades"></div>
  <div class="fill stamp"></div>
  <div class="fill address-line" style="top:250px"></div>
  <div class="fill address-line" style="top:287px"></div>
  <div class="fill address-line" style="top:323px"></div>
</section>

</body>
</html>
```